Handy man Company business card

need branded business card for my new company, this design will transfer to car wrap design what winner will be asked to design

I will need original file so I can edit it in the end.

Also like to have some inspirational quote like "ONE CALL WE DO IT ALL"
"We do it right" can be added to logo side

Like to try to see large 1 800 000 0000 number on front with large logo

Size bigger then standard business card

I like to integrate LAS VEGAS sign to one of sides

Target Market(s)

Handy man services, Home renovation and remodeling

Industry/Entity Type

Handyman

Contact Information for Business Card

Tool Baron LLC.
Name: BORIS LENKOVA
Phone "Temporary": 000 000 0000
Adress: 2715 Fenmore Ct, Las Vegas NV 89147
Website: www.toolbaron.vegas
Email: info@toolbaron.vegas

Requirements
Must have
• Two side
• side n1: LOGO
• side n2: INFO
Nice to have
• Like to have some interesting idea for client to remember!
• With logo added to both side at different stile
Should not have
• Standard design,

```html
<!DOCTYPE html>
<html lang="en">
<head>
<meta charset="utf-8">
<title>Tool Baron LLC. – Business Card</title>
<link href="https://fonts.googleapis.com/css2?family=Poppins:wght@600&family=Roboto:wght@300;400&display=swap" rel="stylesheet">
<style>
  :root {
    --backdrop: #7fcdf3;
    --navy: #1b2a38;
    --orange: #eca229;
    --white: #ffffff;
    --sign-blue: #4f86c6;
    --sign-red: #d8402c;
  }
  * { box-sizing: border-box; margin: 0; padding: 0; }
  html, body {
    width: 1200px; height: 900px; overflow: hidden;
    background: var(--backdrop);
  }
  .sheet {
    width: 1200px; height: 900px;
    display: flex; flex-direction: column;
    align-items: center; justify-content: center; gap: 40px;
  }
  .card {
    width: 760px; height: 390px;
    position: relative; overflow: hidden;
    background: var(--navy);
    box-shadow: 0 10px 26px rgba(20, 60, 90, 0.28);
  }

  /* Front: logo side */
  .card-front {
    display: flex; align-items: center; padding-left: 90px; gap: 30px;
  }
  .mascot {
    width: 130px; height: 170px; border-radius: 16px;
    background: linear-gradient(160deg, var(--orange), #6fb2e0);
    flex-shrink: 0;
  }
  .brand-block { display: flex; flex-direction: column; gap: 34px; }
  .brand-name {
    font-family: "Poppins", sans-serif; font-weight: 600;
    font-size: 72px; line-height: 1; color: var(--white);
    letter-spacing: -1px;
  }
  .phone-pill {
    align-self: flex-end;
    background: var(--orange); color: var(--navy);
    font-family: "Roboto", sans-serif; font-weight: 400;
    font-size: 24px; letter-spacing: 1px;
    padding: 12px 40px; border-radius: 30px;
  }

  /* Back: info side */
  .card-back { display: flex; }
  .vegas-panel {
    width: 46%; height: 100%;
    background: var(--orange);
    display: flex; align-items: center; justify-content: center;
  }
  .vegas-scene {
    width: 300px; height: 290px; border-radius: 14px;
    background: linear-gradient(180deg, #f0b441 0%, var(--sign-blue) 75%, var(--navy) 100%);
  }
  .info-panel {
    flex: 1; padding: 40px 44px;
    display: flex; flex-direction: column; justify-content: space-between;
    text-align: right;
  }
  .contact-list {
    list-style: none;
    font-family: "Roboto", sans-serif; font-weight: 300;
    font-size: 18px; line-height: 1.55; color: var(--white);
  }
  .holder { font-family: "Poppins", sans-serif; font-weight: 600; line-height: 1.2; }
  .company { color: var(--orange); font-size: 27px; }
  .person { color: var(--white); font-size: 27px; }
</style>
</head>
<body>
  <main class="sheet">
    <section class="card card-front" aria-label="Card front">
      <div class="mascot" role="img" aria-label="Cartoon handyman mascot in cap and overalls"></div>
      <div class="brand-block">
        <h1 class="brand-name">Tool Baron</h1>
        <p class="phone-pill">1 800 000 0000</p>
      </div>
    </section>

    <section class="card card-back" aria-label="Card back">
      <div class="vegas-panel">
        <div class="vegas-scene" role="img" aria-label="Welcome to Las Vegas sign illustration with handyman mascot"></div>
      </div>
      <div class="info-panel">
        <ul class="contact-list">
          <li>123 456 7890</li>
          <li>info@toolbaron.vegas</li>
          <li>www.toolbaron.vegas</li>
          <li>2715 Fenmore Ct</li>
          <li>Las Vegas NV 89147</li>
        </ul>
        <div class="holder">
          <p class="company">Tool Baron LLC</p>
          <p class="person">Boris Lenkova</p>
        </div>
      </div>
    </section>
  </main>
</body>
</html>
```